Pilates trainer needs new website

Summary: I need a new, meaningful website in a 1-page format, but one that can be expanded if necessary. I teach in various studios and in the future also in companies. Therefore, the website should convey growth, joy, uniqueness, workout and a bit of luxury.
The website should be inviting.
Layout:
Introduction what I offer
A bit about me
Option to upload price list and timetable in PDF format
Studio address where I teach
The color scheme should be petrol, gold, and colors that match. Not too dark, please.
My current website www.pilates-wendmarau.de, new domain is pilates-corvanel.com (I have already purchased it)
Logo file attached
I have attached a few suggestions but I am also happy to be surprised.

Target Market(s)

Pilates private and small groups,

Industry/Entity Type

Pilates teacher freelancer

Coding

Coded - Design and coding required

Number of Pages Required

1 page

Requirements
Must have
• Welcoming appearance, about me, pictures, offers, colors from the logo but don't get do dark, more fresh and a bit luxurious
Should not have
• Not too wild and going crazy with colors

```html
<!DOCTYPE html>
<html lang="en">
<head>
<meta charset="utf-8">
<title>Pilates Corvanel – Lena Ostwald</title>
<link href="https://fonts.googleapis.com/css2?family=Marcellus&family=Italianno&family=Lora:wght@400;500&display=swap" rel="stylesheet">
<style>
  :root{
    --gold:#c99a45;
    --gold-light:#e2c577;
    --gold-dark:#b0823d;
    --ink:#1d1b18;
    --white:#ffffff;
    --cream:#f6eedf;
    --petrol-deep:#1f4d55;
    --petrol:#2e6b72;
    --petrol-light:#4a8a8e;
  }
  *{margin:0;padding:0;box-sizing:border-box}
  html,body{width:1200px;height:879px;overflow:hidden;background:var(--white)}
  body{position:relative;font-family:'Lora',serif;color:var(--ink)}
  a{text-decoration:none}
  .hero{position:absolute;left:0;top:0;width:1200px;height:590px;overflow:hidden}
  .hero-photo{position:absolute;inset:0;
    background:
      radial-gradient(ellipse 55% 45% at 55% 32%, rgba(214,178,112,.28), transparent 70%),
      radial-gradient(ellipse 60% 50% at 20% 80%, rgba(74,138,142,.45), transparent 70%),
      linear-gradient(180deg,#3b6c72 0%,var(--petrol) 40%,#275c63 70%,var(--petrol-deep) 100%)}
  .hero-wave{position:absolute;left:0;top:0}
  .brand{position:absolute;left:150px;top:48px;width:120px;display:flex;align-items:center;gap:8px;
    font-family:'Marcellus',serif;font-size:17px;color:var(--gold-light);line-height:1.15;text-transform:uppercase;letter-spacing:.6px}
  .brand-dot{width:12px;height:12px;border-radius:50%;background:var(--gold-light);flex:none}
  .nav{position:absolute;top:22px;left:666px;display:flex;align-items:center;
    font-family:'Marcellus',serif;font-size:11.5px;letter-spacing:.9px;color:var(--white);text-transform:uppercase}
  .nav a{color:inherit}
  .nav .home{color:var(--gold-light);text-decoration:underline;text-underline-offset:3px}
  .nav .training{margin-left:28px}
  .nav .about{margin-left:29px}
  .nav .contact{margin-left:37px;background:var(--gold);color:var(--white);border-radius:16px;
    padding:9px 19px 9px}
  .tagline{position:absolute;left:0;width:1200px;top:160px;text-align:center;
    font-family:'Marcellus',serif;font-size:15px;letter-spacing:1.5px;line-height:21px;color:var(--white);text-transform:uppercase}
  .hero-title{position:absolute;left:0;width:1200px;top:220px;text-align:center;
    font-family:'Italianno',cursive;font-weight:400;font-size:68px;line-height:41px;color:var(--gold-light)}
  .cta{position:absolute;left:497px;top:342px;width:207px;height:42px;border-radius:22px;
    background:linear-gradient(90deg,var(--gold-dark),var(--gold-light));
    border:2px solid var(--gold-light);box-shadow:0 0 0 1px var(--petrol-deep) inset;
    font-family:'Marcellus',serif;font-size:10.5px;letter-spacing:.9px;line-height:14px;text-transform:uppercase;
    color:var(--white);text-align:center;padding-top:6px}
  .offer-title{position:absolute;left:0;width:1200px;top:636px;text-align:center;
    font-family:'Italianno',cursive;font-weight:400;font-size:58px;color:var(--gold-dark);line-height:1}
  .offer-text{position:absolute;left:236px;width:728px;top:706px;text-align:center;
    font-size:11.3px;line-height:16.3px}
  .offer-text p+p{margin-top:16px}
  .package{position:absolute;left:330px;top:823px;width:540px;height:70px;border-radius:18px;
    background:linear-gradient(90deg,var(--gold-dark),var(--gold-light));
    border:2px solid var(--gold-dark);box-shadow:0 0 0 2px var(--white) inset;color:var(--white)}
  .package-name{position:absolute;left:33px;top:21px;font-size:17px;font-weight:500}
  .package-info{position:absolute;left:169px;top:15px;font-size:11px;line-height:14px;font-weight:500}
  .package-info span{font-size:9.6px;font-weight:400}
  .package-price{position:absolute;left:388px;top:13px;width:124px;height:32px;border-radius:6px;
    background:var(--cream);color:var(--ink);text-align:right;padding:3px 9px 0;
    font-size:9.8px;line-height:12px}
  .package-price b{color:var(--gold);font-weight:400;font-size:11px}
</style>
</head>
<body>
  <header class="hero">
    <div class="hero-photo" role="img" aria-label="Photo of a bright attic Pilates studio with mats, balls and rollers on a wooden floor"></div>
    <svg class="hero-wave" width="1200" height="590" viewBox="0 0 1200 590">
      <defs>
        <linearGradient id="goldWave" x1="0" x2="1" y1="0" y2="0">
          <stop offset="0" stop-color="#e0c676"/>
          <stop offset="1" stop-color="#c8a15a"/>
        </linearGradient>
      </defs>
      <path d="M500 560 C600 520 680 470 800 465 C880 462 920 490 1000 525 C1080 560 1150 585 1200 570 L1200 590 L500 590 Z" fill="url(#goldWave)"/>
      <path d="M0 556 C30 530 90 528 150 535 C220 545 290 585 370 585 C460 585 560 540 650 510 C720 487 780 470 830 480 C900 495 980 555 1060 575 C1120 590 1170 585 1200 580 L1200 590 L0 590 Z" fill="#ffffff"/>
    </svg>
    <div class="brand"><span class="brand-dot"></span>Pilates Corvanel</div>
    <nav class="nav">
      <a class="home" href="#">Home</a>
      <a class="training" href="#">Training</a>
      <a class="about" href="#">About me</a>
      <a class="contact" href="#">Contact</a>
    </nav>
    <p class="tagline">Change happens through movement<br>and movement heals</p>
    <h1 class="hero-title">Lena Ostwald<br>Pilates Studio trainer</h1>
    <a class="cta" href="#">Request an<br>appointment now</a>
  </header>

  <section>
    <h2 class="offer-title">What i offer</h2>
    <div class="offer-text">
      <p>The first prerequisite for being able to carry out our many different daily tasks with pleasure and joy is physical fitness, a consistently well-trained body and full possession of our mental powers.</p>
      <p>The comprehensive full-body training from Josef Marten helps you achieve exactly this. The aim is to achieve optimal performance of the musculoskeletal system - strength, flexibility and endurance - without risk of injury. Josef Marten originally called his method Contrology: The Art of Control. Contrology is the complete coordination of body, mind and spirit. The basic principles form the basis of all Pilates exercises with one goal: minimum effort - maximum success.</p>
    </div>
    <div class="package">
      <div class="package-name">Starter Paket</div>
      <div class="package-info">Einzeltraining 5 Stunden<br><span>zum Kennenlernen der Pilates Methode</span></div>
      <div class="package-price"><b>350,00€</b><br>nur einmalig möglich</div>
    </div>
  </section>
</body>
</html>
```